Maple & Lantern Flyer

2023 Maple & Lantern
Military, Veterans, Law Enforcement & Fire Fighters
Receive $300* Off Purchased Materials
*$300 maximum discount per order. $3,000 order minimum. Redeem up to 3 times per year.
Terms & Conditions: This program is intended for the professional contractor that supports Brindlecrest Supply with material purchases. One-time purchasers and institutions are not eligible for this program. By choosing to participate, you represent to Brindlecrest Supply that your participation is not prohibited by law. Brindlecrest Supply reserves the right to cancel, suspend, and/or modify this promotion at any time, for any reason, without prior notice. Employees at Brindlecrest Supply are not eligible to participate. All rights reserved by Brindlecrest Supply. Promotion expires December 31, 2023.
Please use our 2023 logo - attached
I'm also attaching the 2022 flyer as an example but looking for a refreshed design!

```html
<!DOCTYPE html>
<html lang="en">
<head>
<meta charset="utf-8">
<title>Maple &amp; Lantern Flyer</title>
<link href="https://fonts.googleapis.com/css2?family=Playfair+Display:wght@800;900&family=Roboto:wght@400;500;700&display=swap" rel="stylesheet">
<style>
  :root {
    --navy: #243179;
    --strip: #2d63b3;
    --white: #ffffff;
    --stage: #d4d4d4;
    --photo-military: linear-gradient(160deg, #c9b38d 0%, #8d8f7a 55%, #3b4660 100%);
    --photo-justice: linear-gradient(160deg, #dfe6ee 0%, #9a8a70 55%, #4a3526 100%);
    --photo-fire: linear-gradient(160deg, #a8322c 0%, #3a3a40 55%, #1c1d24 100%);
  }
  * { box-sizing: border-box; margin: 0; padding: 0; }
  html, body { width: 1200px; height: 2213px; overflow: hidden; }
  body { background: var(--stage); position: relative; font-family: "Roboto", sans-serif; }

  .flyer {
    position: absolute; left: 51px; top: 331px;
    width: 1097px; height: 1550px;
    background: var(--white); overflow: hidden;
    box-shadow: 0 6px 18px rgba(0,0,0,.25);
  }
  .flyer__band {
    position: absolute; left: 0; right: 0; top: 523px; bottom: 0;
    background: var(--navy);
    border-top: 17px solid var(--strip);
  }

  .brand {
    position: absolute; left: 0; right: 0; top: 140px;
    display: flex; align-items: center; justify-content: center; gap: 22px;
    color: var(--navy);
  }
  .brand__dot { width: 56px; height: 56px; border-radius: 50%; background: var(--navy); }
  .brand__name { font-family: "Playfair Display", serif; font-weight: 900; font-size: 64px; }

  .photos { position: absolute; top: 375px; left: 45px; display: flex; gap: 20px; }
  .photo { width: 322px; height: 320px; border-radius: 30px; }
  .photo--military { background: var(--photo-military); }
  .photo--justice { background: var(--photo-justice); }
  .photo--fire { background: var(--photo-fire); }

  .headline {
    position: absolute; left: 0; right: 0; top: 730px;
    text-align: center; color: var(--white);
    font-family: "Playfair Display", serif; font-weight: 900;
    font-size: 66px; letter-spacing: -1px; white-space: nowrap;
  }
  .headline__year { font-size: 92px; letter-spacing: -2px; }

  .audience {
    position: absolute; left: 0; right: 0; top: 848px;
    text-align: center; color: var(--white);
    font-weight: 500; font-size: 50px; line-height: 62px;
  }

  .offer {
    position: absolute; left: 78px; top: 1000px; width: 940px; height: 150px;
  }
  .offer__frame {
    position: absolute; left: 0; right: 0; top: 40px; height: 110px;
    border: 2px solid var(--white);
  }
  .offer__box {
    position: absolute; left: 12px; right: 11px; top: 0; height: 137px;
    background: var(--white);
    display: flex; align-items: center; justify-content: center; gap: 22px;
    color: var(--navy); font-family: "Playfair Display", serif; font-weight: 900;
    padding-bottom: 14px;
  }
  .offer__word { font-size: 82px; }
  .offer__amount { font-size: 108px; letter-spacing: -3px; }
  .offer__tab {
    position: absolute; left: 255px; top: 125px; width: 430px; height: 50px;
    background: var(--white); border-radius: 0 0 18px 18px;
    color: var(--navy); font-weight: 500; font-size: 31px;
    display: flex; align-items: center; justify-content: center;
  }

  .limits {
    position: absolute; left: 107px; top: 1208px; width: 883px; height: 119px;
    border: 2px solid var(--white);
    display: flex; align-items: center; justify-content: center;
    text-align: center; color: var(--white); font-size: 30px; line-height: 38px;
  }

  .terms {
    position: absolute; left: 45px; right: 45px; top: 1358px;
    text-align: center; color: var(--white); font-size: 19.5px; line-height: 24.5px;
  }
  .terms strong { font-weight: 700; }
</style>
</head>
<body>
  <main class="flyer">
    <div class="flyer__band"></div>

    <header class="brand">
      <span class="brand__dot"></span>
      <span class="brand__name">Brindlecrest Supply</span>
    </header>

    <section class="photos">
      <div class="photo photo--military" role="img" aria-label="Photo of a military family standing by a gate with a flag"></div>
      <div class="photo photo--justice" role="img" aria-label="Photo of a Lady Justice statue with gavel and book"></div>
      <div class="photo photo--fire" role="img" aria-label="Photo of a firefighter placing a helmet on a child"></div>
    </section>

    <h1 class="headline"><span class="headline__year">2023</span> MAPLE &amp; LANTERN</h1>

    <p class="audience">MILITARY, VETERANS, LAW<br>ENFORCEMENT &amp; FIRE FIGHTERS</p>

    <div class="offer">
      <div class="offer__frame"></div>
      <div class="offer__box">
        <span class="offer__word">RECEIVE</span>
        <span class="offer__amount">$300</span>
        <span class="offer__word">OFF</span>
      </div>
      <div class="offer__tab">PURCHASED MATERIALS</div>
    </div>

    <p class="limits">$300 maximum discount per order. $3,000 order minimum.<br>Redeem up to 3 times per year.</p>

    <p class="terms"><strong>Terms &amp; Conditions:</strong> This program is intended for the professional contractor that supports Brindlecrest Supply with material purchases. One-time purchasers and institutions are not eligible for this program. By choosing to participate, you represent to Brindlecrest Supply that your participation is not prohibited by law. Brindlecrest Supply reserves the right to cancel, suspend, and/or modify this promotion at any time, for any reason, without prior notice. Employees at Brindlecrest Supply are not eligible to participate. All rights reserved by Brindlecrest Supply. Promotion expires December 31, 2023.</p>
  </main>
</body>
</html>
```